Aged Care Consultancy Business needs a business card design

I need a two sided business card - I want it clean and professional. Surprise me

Target Market(s)

middle aged and ageing victorians

Industry/Entity Type

Health Care

Contact Information for Business Card

Text to be included

Logo
Aged Care Consulting Services
Professional, Reliable, Affordable

Tovan Brelsick
Director
0427 31 64 92 (larger)
1300 73 29 41
tovan@wadolire.com.au
www.wadolcare.com.au
Facebook (details TBA)

include little icons beside the contact info:

- Envelope = email
- Phone = phone
- Globe = website

Font styles to use
Serif
Sans Serif

Requirements
Must have
• look proffesional and clean

```html
<!DOCTYPE html>
<html lang="en">
<head>
<meta charset="utf-8">
<title>wadol care — Business Card</title>
<link rel="stylesheet" href="https://fonts.googleapis.com/css2?family=Fira+Sans:wght@400;500;600;700&display=swap">
<style>
  :root {
    --backdrop: #4f5359;
    --navy: #1a437e;
    --navy-deep: #133564;
    --orange: #e69024;
    --paper: #ffffff;
    --ink: #4a4a4a;
  }
  * { margin: 0; padding: 0; box-sizing: border-box; }
  html, body {
    width: 1200px; height: 1200px; overflow: hidden;
    background: var(--backdrop);
    font-family: "Fira Sans", sans-serif;
  }
  .canvas { position: relative; width: 1200px; height: 1200px; }
  .card {
    position: absolute; left: 140px;
    width: 920px; height: 526px; overflow: hidden;
  }
  .card--back { top: 48px; background: var(--navy); }
  .card--front { top: 626px; background: var(--paper); }
  .card svg.bands { position: absolute; inset: 0; }

  .back-brand {
    position: absolute; left: 0; right: 0; top: 190px;
    text-align: center;
    font-size: 104px; font-weight: 700; letter-spacing: 1px;
    color: var(--navy-deep);
  }

  .front-brand {
    position: absolute; right: 80px; top: 84px;
    display: flex; align-items: center; gap: 18px;
    font-size: 78px; font-weight: 700; color: var(--navy);
  }
  .front-brand .dot {
    width: 26px; height: 26px; border-radius: 50%; background: var(--orange);
  }

  .contact { position: absolute; left: 72px; bottom: 118px; color: var(--ink); }
  .contact .name {
    font-size: 44px; font-weight: 700; color: var(--navy);
    letter-spacing: 0.5px; text-transform: uppercase; line-height: 1.15;
  }
  .contact .role { font-size: 30px; margin-top: 2px; line-height: 1.2; }
  .contact .role .mobile { font-size: 38px; }
  .contact .lines { margin-top: 20px; font-size: 27px; line-height: 1.3; }
  .contact .line { display: flex; align-items: center; gap: 8px; }
  .contact .icon { width: 26px; height: 26px; flex: none; fill: var(--navy); }
  .contact .sep { margin: 0 6px; }

  .social {
    position: absolute; right: 60px; top: 318px;
    width: 64px; height: 64px; border-radius: 8px; background: var(--navy);
  }
</style>
</head>
<body>
<main class="canvas">

  <section class="card card--back" aria-label="Card back">
    <svg class="bands" viewBox="0 0 920 526" aria-hidden="true">
      <polygon points="920,330 920,526 640,526" fill="var(--paper)"/>
      <polygon points="920,372 920,526 710,526" fill="var(--orange)"/>
    </svg>
    <div class="back-brand">wadol care</div>
  </section>

  <section class="card card--front" aria-label="Card front">
    <svg class="bands" viewBox="0 0 920 526" aria-hidden="true">
      <polyline points="0,432 590,432 612,448 920,448" fill="none" stroke="var(--navy)" stroke-width="2"/>
      <polygon points="0,446 588,446 640,526 0,526" fill="var(--navy)"/>
      <polygon points="606,460 920,460 920,526 656,526" fill="var(--orange)"/>
    </svg>

    <div class="front-brand"><span class="dot"></span>wadol care</div>

    <div class="contact">
      <div class="name">Tovan Brelsick</div>
      <div class="role">Director | <span class="mobile">0427 31 64 92</span></div>
      <div class="lines">
        <div class="line">
          <svg class="icon" viewBox="0 0 24 24" aria-hidden="true"><path d="M3 9c0-3 4-5 9-5s9 2 9 5v2h-5V9H8v2H3zM6 12h12l2 8H4z"/><circle cx="12" cy="16" r="2.5" fill="#fff"/></svg>
          1300 73 29 41
        </div>
        <div class="line">
          <svg class="icon" viewBox="0 0 24 24" aria-hidden="true"><path d="M2 5h20v14H2z"/><path d="M2 5l10 8 10-8" fill="none" stroke="#fff" stroke-width="1.6"/></svg>
          tovan@wadolire.com.au
          <span class="sep">|</span>
          <svg class="icon" viewBox="0 0 24 24" aria-hidden="true"><circle cx="12" cy="12" r="10"/><path d="M2 12h20M12 2c-4 4-4 16 0 20M12 2c4 4 4 16 0 20" fill="none" stroke="#fff" stroke-width="1.4"/></svg>
          www.wadolcare.com.au
        </div>
      </div>
    </div>

    <div class="social" aria-hidden="true"></div>
  </section>

</main>
</body>
</html>
```